Real Estate Business card design

Company Name: Tamarind Holdings, LLC
subtitle: We pay cash for houses!
Daniel Whitcombe
Managing Director
555-214-0963
Dan@TamarindHoldingsLLC.example
www.TamarindHoldingsLLC.example

We pay referral fees for Seller and Buyer leads.

Back:
We offer referral fees for Seller and Buyer leads that close.

Please contact Hal at 555-214-0963 with your referrals or to learn more about the referral program!

I am open to different color options but I am going for a classic, elegant, clean, and professional look. Please use logo as a reference.

Target Market(s)

People selling their homes and people in the market for buying homes.

Contact Information for Business Card

please see project description

Font styles to use
Serif
Sans Serif
Script

Requirements
Must have
• must have my logo in it
Nice to have
• I like cards that are split down the middle but please come up with a few mock ups. Open to any color scheme.

```html
<!DOCTYPE html>
<html lang="en">
<head>
<meta charset="utf-8">
<title>Tamarind Holdings – Business Card</title>
<link rel="stylesheet" href="https://fonts.googleapis.com/css2?family=Source+Sans+3:wght@400;600;700&display=swap">
<style>
  :root {
    --bg: #2a2b2e;
    --paper: #ffffff;
    --paper-shade: #f1f1f1;
    --gold: #c49a64;
    --slate: #3b4150;
    --ink: #3d3f45;
    --white: #ffffff;
  }
  * { box-sizing: border-box; margin: 0; padding: 0; }
  html, body {
    width: 1200px; height: 874px; overflow: hidden;
    background: var(--bg);
    font-family: "Source Sans 3", "Myriad Pro", sans-serif;
  }
  .sheet { position: relative; width: 1200px; height: 874px; }
  .card {
    position: absolute; left: 250px; width: 700px; height: 400px;
    background: linear-gradient(160deg, var(--paper) 55%, var(--paper-shade));
    overflow: hidden;
    box-shadow: 0 10px 24px rgba(0,0,0,.35);
  }
  .card--back { top: 22px; }
  .card--front { top: 452px; }

  /* Back */
  .referral-headline {
    position: absolute; top: 52px; left: 0; right: 0;
    text-align: center; color: var(--gold);
    font-size: 25px; line-height: 1.25; font-weight: 400;
  }
  .referral-headline strong { font-weight: 700; }
  .divider {
    position: absolute; top: 190px; left: 300px; width: 100px; height: 3px;
    background: var(--gold);
  }
  .referral-contact {
    position: absolute; bottom: 56px; left: 0; right: 0;
    text-align: center; color: var(--ink);
    font-size: 17px; line-height: 1.35;
  }
  .referral-contact strong { color: var(--gold); font-weight: 700; }

  /* Front */
  .brand { position: absolute; top: 70px; left: 48px; }
  .brand-name {
    display: flex; align-items: center; gap: 12px;
    font-size: 30px; font-weight: 600; color: var(--slate);
  }
  .brand-mark { width: 14px; height: 14px; background: var(--gold); }
  .brand-tagline {
    margin-top: 6px; margin-left: 26px;
    font-size: 17px; font-weight: 600; color: var(--slate);
  }
  .front-bands { position: absolute; inset: 0; }
  .contact-block {
    position: absolute; right: 44px; top: 232px; text-align: right;
    color: var(--white);
  }
  .person-name { font-size: 28px; font-weight: 700; letter-spacing: .3px; }
  .person-title { font-size: 17px; color: var(--gold); margin-top: -2px; }
  .contact-list { list-style: none; margin-top: 12px; font-size: 16px; line-height: 1.55; }
  .contact-list li { display: flex; justify-content: flex-end; align-items: center; gap: 8px; }
  .contact-icon { width: 14px; height: 14px; flex: none; }
</style>
</head>
<body>
<main class="sheet">

  <section class="card card--back" aria-label="Card back">
    <p class="referral-headline">We offer <strong>Referral Fees for Seller &amp; Buyer</strong><br>leads That Close.</p>
    <div class="divider"></div>
    <p class="referral-contact">Please <strong>Contact Hal at 555-214-0963 with your referrals</strong> or<br>to learn more about the Referral program!</p>
  </section>

  <section class="card card--front" aria-label="Card front">
    <div class="brand">
      <div class="brand-name"><span class="brand-mark"></span>Tamarind Holdings, LLC</div>
      <div class="brand-tagline">We Pay Cash For Houses</div>
    </div>

    <svg class="front-bands" width="700" height="400" viewBox="0 0 700 400" aria-hidden="true">
      <polygon points="0,292 700,70 700,150 0,300" fill="var(--gold)"/>
      <polygon points="0,312 700,166 700,400 0,400" fill="var(--slate)"/>
    </svg>

    <div class="contact-block">
      <div class="person-name">Daniel Whitcombe</div>
      <div class="person-title">Managing Director</div>
      <ul class="contact-list">
        <li>555-214-0963
          <svg class="contact-icon" viewBox="0 0 16 16"><path fill="var(--gold)" d="M3.5 1.5l2.5 0 1 3.5-1.7 1.2a9 9 0 0 0 4.5 4.5L11 9l3.5 1v2.5A2 2 0 0 1 12.5 14.5 11 11 0 0 1 1.5 3.5 2 2 0 0 1 3.5 1.5z"/></svg>
        </li>
        <li>Dan@TamarindHoldingsLLC.example
          <svg class="contact-icon" viewBox="0 0 16 16"><rect x="1" y="3" width="14" height="10" rx="1" fill="var(--gold)"/><path d="M1.5 3.8L8 9l6.5-5.2" stroke="var(--slate)" stroke-width="1.3" fill="none"/></svg>
        </li>
        <li>www.TamarindHoldingsLLC.example
          <svg class="contact-icon" viewBox="0 0 16 16"><circle cx="8" cy="8" r="7" fill="var(--gold)"/><path d="M1 8h14M8 1c-3 3.5-3 10.5 0 14M8 1c3 3.5 3 10.5 0 14" stroke="var(--slate)" stroke-width="1.1" fill="none"/></svg>
        </li>
      </ul>
    </div>
  </section>

</main>
</body>
</html>
```